New Massage Business needs a Card design

We need a card design for our new massage therapy business based in Sydney, Au. The business is getting a makeover, so a little later on we'll need shirts, various pamphlets and promotional flyers, and possibly a website. The winner will be offered those jobs as well.

Colour scheme should be green, black, and steel/charcoal grey. The business focuses on massage as an anatomical solution to stress, muscle aches, pains and fatigue. Ideally we'd like an anatomical image of the muscle system (ref to the attached files). In my mind this image takes up most of the left third of the card, and shows points of tension and pain at the neck and lower back. This image should be the grey portion of the card.

On the upper right is the other image attached, with a simple line drawing of a vehicle on the left end of the line, and a building on the right end replacing the stick figure (we have a therapist specializing in mobile massage). The blank part in the middle of the line should have "Kestrel Wellness", and in smaller writing below, "The Tension Fix".

Bottom right corner should have the contact and business details.
On the back we'd like a "next appointment" and "refer a friend" option.

If you have a design which doesn't fit the above, but you feel suits the business, please submit anyway - sometimes you don't know what you like until you see it.

Business Details:
Name: Kestrel Wellness - The Tension Fix

Industry/Entity Type

Massage Therapy

Contact Information for Business Card

Business Details:
Contact name: Marcus
Title: Massage Therapist
Contact: 0458203617
Email: info@ktfbodywork.example

Requirements
Must have
• Colour scheme should be green, black, and steel/charcoal grey. The business focuses on massage as an anatomical solution to stress, muscle aches, pains and fatigue. Ideally we'd like an anatomical image of the muscle system (ref to the attached files). In my mind this image takes up most of the left third of the card, and shows points of tension and pain at the neck and lower back. This image should be the grey portion of the card.
• On the upper right is the other image attached, with a simple line drawing of a vehicle on the left end of the line, and a building on the right end replacing the stick figure (we have a therapist specializing in mobile massage). The blank part in the middle of the line should have "Kestrel Wellness", and in smaller writing below, "The Tension Fix".
• Bottom right corner should have the contact and business details.
• On the back we'd like a "next appointment" and "refer a friend" option.
Nice to have
• Matt finish - no gloss
• If you have a design which doesn't fit the above, but you feel suits the business, please submit anyway - sometimes you don't know what you like until you see it.
Should not have
• Anything 'Zen'. The business promotes the physiological and scientific benefits of massage. For clients with spiritual or meditative needs, we refer out.

```html
<!DOCTYPE html>
<html lang="en">
<head>
<meta charset="utf-8">
<title>Kestrel Wellness – Business Card</title>
<link rel="stylesheet" href="https://fonts.googleapis.com/css2?family=Source+Sans+3:wght@400;600&display=swap">
<style>
  :root {
    --backdrop: #a8a8a8;
    --card-black: #151515;
    --lime: #c3e84f;
    --lime-card: #c1e853;
    --charcoal: #3f3f3f;
    --point-fill: #444444;
    --point-ring: #555555;
  }
  * { box-sizing: border-box; margin: 0; padding: 0; }
  html, body { width: 1200px; height: 1000px; overflow: hidden; }
  body {
    background: var(--backdrop);
    font-family: "Source Sans 3", "Myriad Pro", sans-serif;
    position: relative;
  }
  .card {
    position: absolute;
    width: 734px;
    height: 418px;
    overflow: hidden;
  }
  .card-front { left: 108px; top: 40px; background: var(--card-black); }
  .card-back  { left: 344px; top: 527px; background: var(--lime-card); }

  .front-art { position: absolute; inset: 0; }

  .brand-front {
    position: absolute;
    top: 51px;
    left: 469px;
    width: 200px;
    text-align: center;
    color: var(--lime);
    font-weight: 600;
  }
  .brand-front .brand-name { font-size: 18px; line-height: 20px; }
  .brand-front .brand-tagline { font-size: 9px; line-height: 11px; }

  .contact {
    position: absolute;
    right: 53px;
    top: 227px;
    text-align: right;
    color: var(--lime);
    white-space: nowrap;
  }
  .contact-name { font-size: 35px; font-weight: 600; line-height: 36px; }
  .contact-title { font-size: 25px; font-weight: 400; line-height: 34px; margin-bottom: 20px; }
  .contact-line { font-size: 21px; font-weight: 400; line-height: 25px; }

  .back-field {
    position: absolute;
    left: 53px;
    font-size: 21px;
    line-height: 26px;
    color: var(--charcoal);
  }
  .field-next { top: 50px; }
  .field-refer { top: 288px; }

  .brand-back {
    position: absolute;
    left: 0; right: 0;
    top: 176px;
    text-align: center;
    color: var(--charcoal);
    font-weight: 600;
  }
  .brand-back .brand-name { font-size: 36px; line-height: 42px; }
  .brand-back .brand-tagline { font-size: 17px; line-height: 22px; }
</style>
</head>
<body>

<section class="card card-front" aria-label="Card front">
  <svg class="front-art" width="734" height="418" viewBox="0 0 734 418">
    <defs>
      <linearGradient id="artTone" x1="0" y1="0" x2="1" y2="0">
        <stop offset="0" stop-color="#dcdcdc"/>
        <stop offset="1" stop-color="#9a9a9a"/>
      </linearGradient>
    </defs>
    <path class="swoosh swoosh-main" fill="var(--lime)"
          d="M118 310 C300 318 460 352 560 418 H522 C440 372 300 334 118 324 Z"/>
    <path class="swoosh swoosh-inner" fill="var(--lime)"
          d="M262 364 C350 378 430 398 475 418 H458 C410 400 340 382 262 368 Z"/>
    <path class="swoosh swoosh-rise" fill="var(--lime)"
          d="M440 418 C560 412 670 402 734 392 V418 Z"/>
    <rect class="anatomy-area" role="img" aria-label="Anatomical illustration of the back and shoulder muscles"
          x="0" y="0" width="215" height="418" fill="url(#artTone)"/>
    <g class="tension-point tension-neck">
      <circle cx="32" cy="36" r="32" fill="none" stroke="var(--point-ring)" stroke-width="3"/>
      <circle cx="32" cy="36" r="22" fill="var(--point-fill)"/>
    </g>
    <g class="tension-point tension-lower-back">
      <circle cx="72" cy="350" r="32" fill="none" stroke="var(--point-ring)" stroke-width="3"/>
      <circle cx="72" cy="350" r="22" fill="var(--point-fill)"/>
    </g>
  </svg>

  <div class="brand-front">
    <div class="brand-name">Kestrel Wellness</div>
    <div class="brand-tagline">The Tension Fix</div>
  </div>

  <div class="contact">
    <div class="contact-name">Marcus</div>
    <div class="contact-title">Massage Therapist</div>
    <div class="contact-line">0458203617</div>
    <div class="contact-line">info@ktfbodywork.example</div>
  </div>
</section>

<section class="card card-back" aria-label="Card back">
  <p class="back-field field-next">Next appointment:</p>
  <div class="brand-back">
    <div class="brand-name">Kestrel Wellness</div>
    <div class="brand-tagline">The Tension Fix</div>
  </div>
  <p class="back-field field-refer">Refer a friend:</p>
</section>

</body>
</html>
```